Create Direct Mail Flyer For House Painting Company

The flyer needs to promote "Free Cheese For A Season" (When they paint their whole house. We want to Focus on the offer, also a free colour consultation, the awards and the guarantees! This will be a full colour 2 sided letter box drop flyer.
This is an emotional Direct Response flyer. I want the Headline to be Bold and stand out. Follow the branding if the website https://larkwoodresurfacing.com.au/
I have attached some social media photos to show you the promotion idea of Free Cheese For A Season. Use better photos if you have them.
I have given you a number of photos to use on the brochure, use your skills to determine what you feel is best to use. Also with the Colour consultation points use small photos to emphasise the points.
Have the testimonials and the team photo on the back.
Also have urgency. ACT NOW -OFFER ENDING SOON!

Target Market(s)

Home Owners

Industry/Entity Type

House Painting, Roof Painting

Colors
0054AA
0677BA
7BADD7
CADEEF
E8F1F8

Requirements
Must have
• Keep the Brand Colours. I have attached a sample flyer that shows a concept that I like. Have the testimonials on the back of the flyer. I do not want the flyer to look to busy.

```html
<!DOCTYPE html>
<html lang="en">
<head>
<meta charset="utf-8">
<title>Larkwood Resurfacing – Free Cheese For A Season Flyer</title>
<link rel="stylesheet" href="https://fonts.googleapis.com/css2?family=Bebas+Neue&family=Raleway:wght@400;500;600;700&display=swap">
<style>
:root{
  --stage:#5c5c5c;
  --brand-deep:#0054AA;
  --brand:#0677BA;
  --brand-mid:#1a8cc6;
  --brand-light:#7BADD7;
  --brand-pale:#CADEEF;
  --brand-mist:#E8F1F8;
  --slate:#6a767d;
  --ink:#1e1e1e;
  --text:#3a3a3a;
  --muted:#8a8a8a;
  --white:#ffffff;
}
*{box-sizing:border-box;margin:0;padding:0}
html,body{width:1020px;height:1200px;overflow:hidden;background:var(--stage)}
body{position:relative;font-family:"Raleway",sans-serif;color:var(--text)}
.side{position:absolute;top:80px;width:401px;height:1040px;overflow:hidden;box-shadow:0 8px 10px rgba(0,0,0,.35)}
.side--front{left:91px;background:var(--brand-mid)}
.side--back{left:528px;background:var(--white)}
.abs{position:absolute}

/* front */
.hero-sky{left:0;top:0;width:401px;height:520px;background:linear-gradient(180deg,#f4f6f8 0%,#e6ebef 30%,#cfd8df 60%,#8f9aa0 100%)}
.hero-photo{left:0;top:205px;width:401px;height:315px;background:linear-gradient(160deg,#c9d3da 0%,#a6acae 35%,#7d7a72 60%,#5a6b3c 100%)}
.brush-edge{left:0;top:500px;width:401px;height:40px}
.headline{left:21px;top:48px;font-family:"Bebas Neue",sans-serif;font-weight:400;font-size:36px;line-height:34px;color:var(--ink);white-space:nowrap}
.intro{left:21px;top:156px;width:372px;font-size:10.8px;line-height:14.4px;color:var(--ink)}
.brand-lockup{display:flex;align-items:center;gap:6px}
.brand-lockup .mark{width:14px;height:14px;background:var(--brand)}
.brand-lockup .name{font-family:"Raleway",sans-serif;font-weight:700;color:var(--brand);letter-spacing:1px}
.front-logo{right:14px;top:44px}
.front-logo .name{font-size:17px}
.steps-banner{left:21px;top:527px;width:360px;height:34px;background:var(--white);border:2px solid var(--brand-pale);box-shadow:0 3px 0 rgba(0,40,90,.35);font-family:"Bebas Neue",sans-serif;font-size:26px;line-height:32px;text-align:center;color:var(--brand)}
.step{left:19px;width:372px}
.step-photo{position:absolute;left:0;top:0;width:89px;height:76px}
.step-num{position:absolute;left:2px;bottom:-4px;font-family:"Bebas Neue",sans-serif;font-size:38px;color:var(--white);-webkit-text-stroke:1px #333}
.step-body{margin-left:97px}
.step-title{font-family:"Bebas Neue",sans-serif;font-weight:400;font-size:19px;color:var(--white);line-height:20px;margin-bottom:4px}
.step-text{font-size:10.2px;line-height:14.1px;color:var(--white)}

/* back */
.back-top{left:0;top:0;width:401px;height:200px;background:var(--slate)}
.offer-heading{left:29px;top:18px;font-family:"Bebas Neue",sans-serif;font-weight:400;font-size:23px;line-height:21px;color:var(--white)}
.col{top:68px;color:var(--white)}
.col h3{font-weight:500;font-size:15px;margin-bottom:4px}
.col ul{list-style:none}
.col li{position:relative;padding-left:24px;font-size:11px;line-height:15px}
.col li::before{content:"";position:absolute;left:0;top:4px;width:8px;height:8px;border-radius:50%;background:#1b1b1b}
.col--services{left:29px;width:160px}
.col--guarantees{left:219px;width:160px}
.testimonials-title{left:0;top:184px;width:401px;text-align:center;font-family:"Bebas Neue",sans-serif;font-weight:400;font-size:34px;letter-spacing:9px;color:var(--brand)}
.review{left:44px;width:335px;font-size:5.6px;line-height:8.6px;color:#555}
.review .avatar{position:absolute;left:0;top:0;width:19px;height:19px;border-radius:50%;color:var(--white);font-size:9px;line-height:19px;text-align:center}
.review .body{margin-left:24px}
.review .who{font-weight:700;font-size:6px;color:#222}
.review .meta{color:var(--muted)}
.review .stars{color:#f3a712;letter-spacing:.5px}
.review .stars span{color:var(--muted);margin-left:4px}
.review b{color:#333}
.review .more{position:absolute;right:0;top:2px;color:#777}
.review-photos{display:flex;gap:2px;margin:5px 0 8px}
.review-photos div{width:47px;height:47px}
.back-band{left:0;top:665px;width:401px;height:195px;background:var(--slate)}
.team-photo{top:686px;height:106px}
.award{top:797px;height:35px;background:linear-gradient(90deg,#efe6c8,#d6bb6b);border:1px solid #fff}
.award--plain{background:#f5f5f5}
.call-title{left:148px;top:876px;font-weight:600;font-size:15.5px;line-height:17px;color:var(--ink)}
.call-pill{left:148px;top:918px;width:241px;height:27px;border-radius:14px;background:var(--brand);color:var(--white);font-weight:600;font-size:14px;line-height:27px;padding-left:35px}
.call-pill svg{position:absolute;left:12px;top:5px}
.contact{left:152px;font-size:9.6px;color:var(--ink);display:flex;align-items:center;gap:4px}
.back-logo{left:14px;top:930px}
.back-logo .name{font-size:17px}
.urgency{left:60px;top:1000px;width:280px;height:34px;border:2px solid var(--brand);background:var(--white);box-shadow:0 3px 0 rgba(0,40,90,.3);font-family:"Bebas Neue",sans-serif;font-size:28px;line-height:32px;text-align:center;color:var(--brand)}
</style>
</head>
<body>

<section class="side side--front">
  <div class="abs hero-sky"></div>
  <div class="abs hero-photo" role="img" aria-label="Freshly painted two-storey home with a cheese platter in the foreground and a page-curl reveal"></div>
  <svg class="abs brush-edge" viewBox="0 0 401 40" preserveAspectRatio="none" aria-hidden="true">
    <path d="M0 20 L40 14 L70 18 L110 10 L150 16 L190 8 L230 14 L270 4 L300 12 L340 2 L370 10 L401 6 L401 40 L0 40 Z" fill="var(--brand-mid)"/>
  </svg>
  <div class="abs brand-lockup front-logo"><span class="mark"></span><span class="name">LARKWOOD</span></div>
  <h1 class="abs headline">Transform<br>Your Home And<br>Get Free Cheese For A Season!</h1>
  <p class="abs intro">Paint your whole house with us and receive a free colour consultation to ensure the perfect shade. Plus, enjoy a taste of fine cheese every week for a season, on us. Our skilled painters are ready to transform your home.</p>

  <div class="abs steps-banner">Four Steps To Bring Your Vision To Life!</div>

  <div class="abs step" style="top:583px">
    <div class="step-photo" role="img" aria-label="Homeowners browsing paint colour swatches" style="background:linear-gradient(135deg,#dfe3e8,#c9a77f 60%,#e9c34a)"><span class="step-num">1</span></div>
    <div class="step-body">
      <h2 class="step-title">Consider The Mood You Want To Create:</h2>
      <p class="step-text">Think about the atmosphere you want to evoke in each room. Do you want a calming and relaxing space, or a vibrant and energizing one? Choose colours that align with the mood you want to create.</p>
    </div>
  </div>

  <div class="abs step" style="top:681px">
    <div class="step-photo" role="img" aria-label="Living room with a turquoise feature wall" style="background:linear-gradient(135deg,#3fa7b8,#5fbac6 55%,#6b4c3e)"><span class="step-num">2</span></div>
    <div class="step-body">
      <h2 class="step-title">Look At The Room's Natural Light:</h2>
      <p class="step-text">Take note of the amount and direction of natural light in each room. Light affects how colours appear, so you'll want to choose shades that complement the lighting. For example, warm hues like red and orange work well in rooms with a lot of natural light, while cool hues like blue and green are better suited for rooms with less light.</p>
    </div>
  </div>

  <div class="abs step" style="top:808px">
    <div class="step-photo" role="img" aria-label="Kitchen painted in warm yellow" style="background:linear-gradient(135deg,#c99a1e,#e8b93a 50%,#f3ead2)"><span class="step-num">3</span></div>
    <div class="step-body">
      <h2 class="step-title">Think About The Room's Function:</h2>
      <p class="step-text">Consider the purpose of each room and choose colours that align with the function. For instance, blue or green may be suitable for a bedroom to create a calming environment, while yellow or orange may work well in a kitchen to add warmth and energy.</p>
    </div>
  </div>

  <div class="abs step" style="top:918px">
    <div class="step-photo" role="img" aria-label="Test paint patches in yellow, pink and teal on a wall" style="background:linear-gradient(90deg,#f4f4f4 15%,#f2d63a 35%,#ec6a9a 55%,#38b8d2 75%,#f4f4f4)"><span class="step-num">4</span></div>
    <div class="step-body">
      <h2 class="step-title">Test The Colours:</h2>
      <p class="step-text">Once you've narrowed down your choices, test them out in the room. Paint a small patch on the wall and observe how it looks at different times of the day and in different lighting conditions. This will help you determine if the colour is right for the space.</p>
    </div>
  </div>
</section>

<section class="side side--back">
  <div class="abs back-top"></div>
  <svg class="abs" style="left:0;top:170px" width="401" height="50" viewBox="0 0 401 50" aria-hidden="true">
    <path d="M0 28 L20 22 L60 16 L100 18 L140 10 L180 16 L230 8 L280 14 L330 6 L370 14 L401 18 L401 50 L0 50 Z" fill="var(--white)"/>
  </svg>
  <h2 class="abs offer-heading">Grab Your Free Cheese And Colour<br>Consultation While This Offer Lasts.</h2>
  <div class="abs col col--services">
    <h3>OUR SERVICES</h3>
    <ul><li>Roof Restoration and Painting</li><li>House Painting</li><li>Epoxy Floors</li></ul>
  </div>
  <div class="abs col col--guarantees">
    <h3>OUR GUARANTEES</h3>
    <ul><li>On Time Guarantee</li><li>White Glove Cleanliness Guarantee</li><li>15 Year Guarantee</li><li>Satisfaction Guarantee</li></ul>
  </div>

  <h2 class="abs testimonials-title">Testimonials</h2>

  <article class="abs review" style="top:228px">
    <div class="avatar" style="background:#8a8f93">T</div>
    <span class="more">⋮</span>
    <div class="body">
      <div class="who">Tom Hallam</div>
      <div class="meta">Local Guide · 6 reviews · 11 photos</div>
      <div class="stars">★★★★★<span>5 months ago</span></div>
      <p><b>Positive:</b> Professionalism, Punctuality, Quality, Responsiveness, Value</p>
      <p style="margin-top:5px">Neil Carver and his team are true professionals. Neil sent his A team lead by Briggs to paint the interior and exterior of our new build. The attention to detail is exceptional, best paint team I have ever used. I would not hesitate to use them on all our future projects and would not hesitate to recommend them. Thx Larkwood team your super stars - not just 5 stars</p>
      <p style="margin-top:5px"><b>Services:</b> Exterior painting, Interior painting</p>
    </div>
  </article>

  <article class="abs review" style="top:337px">
    <div class="avatar" style="background:#2f8f3a">M</div>
    <span class="more">⋮</span>
    <div class="body">
      <div class="who">Mia Castellan</div>
      <div class="meta">3 reviews</div>
      <div class="stars">★★★★★<span>3 months ago</span></div>
      <p><b>Positive:</b> Professionalism, Punctuality, Quality, Responsiveness, Value</p>
      <p style="margin-top:5px">Most professional painters we have ever dealt with from precision of work, tidiness, promptness, reliable company that followed up all queries immediately and with politeness at all times.</p>
      <p style="margin-top:5px"><b>Services:</b> Interior painting, Exterior painting</p>
    </div>
  </article>

  <article class="abs review" style="top:426px">
    <div class="avatar" style="background:#ef7b22">J</div>
    <span class="more">⋮</span>
    <div class="body">
      <div class="who">Jo Whitfield</div>
      <div class="meta">1 review · 3 photos</div>
      <div class="stars">★★★★★<span>3 months ago</span></div>
      <p><b>Positive:</b> Professionalism, Punctuality, Quality</p>
      <p style="margin-top:5px">Recently had the exterior of my home and deck painted. The painters who came were very professional and friendly. Would not hesitate to recommend them for any painting requirements you might have.</p>
      <p style="margin-top:5px"><b>Service:</b> Exterior painting</p>
      <div class="review-photos">
        <div role="img" aria-label="Freshly painted house exterior" style="background:linear-gradient(135deg,#3c4148,#8d9aa3)"></div>
        <div role="img" aria-label="Painted weatherboard cottage" style="background:linear-gradient(135deg,#7fa6c4,#d5dde2)"></div>
        <div role="img" aria-label="Painted deck with garden" style="background:linear-gradient(135deg,#2d3b2e,#9aa8ae)"></div>
      </div>
      <p>👍 Like</p>
    </div>
  </article>

  <article class="abs review" style="top:580px">
    <div class="avatar" style="background:#5a62c9">R</div>
    <span class="more">⋮</span>
    <div class="body">
      <div class="who">Rosa M</div>
      <div class="meta">5 reviews</div>
      <div class="stars">★★★★★<span>4 months ago</span></div>
      <p style="margin-top:4px">Repaired and sealed my tile roof and repainted my water stained ceilings. Fast quote, fast turnaround on the job - in fact they got it done 2 weeks earlier than promised. Dex and team did a great job, were trustworthy with full access to my home while I was at work and comms with admin were great. Larkwood weren't my cheapest quote but were within 10% and what swung it for me was the 15year Colourline guarantee on the work. Can certainly recommend.</p>
    </div>
  </article>

  <div class="abs back-band"></div>
  <svg class="abs" style="left:0;top:645px" width="401" height="40" viewBox="0 0 401 40" aria-hidden="true">
    <path d="M0 0 L401 0 L401 32 L370 24 L330 30 L290 18 L240 24 L200 14 L150 22 L100 16 L60 22 L20 14 L0 18 Z" fill="var(--white)"/>
  </svg>
  <div class="abs team-photo" role="img" aria-label="Team members at an awards night" style="left:69px;width:62px;background:linear-gradient(180deg,#4a3b26,#2b2b33 60%,#1d1d22)"></div>
  <div class="abs team-photo" role="img" aria-label="Painting crew standing with branded vehicles" style="left:150px;width:181px;background:linear-gradient(180deg,#9ec6e6 0%,#cfe2ef 35%,#2f5f9e 60%,#3a3f44 100%)"></div>
  <div class="abs award" style="left:69px;width:120px"></div>
  <div class="abs award award--plain" style="left:191px;width:69px"></div>
  <div class="abs award award--plain" style="left:262px;width:69px"></div>
  <svg class="abs" style="left:0;top:840px" width="401" height="40" viewBox="0 0 401 40" aria-hidden="true">
    <path d="M0 40 L0 14 L30 8 L70 16 L120 10 L170 18 L220 8 L270 16 L320 12 L370 20 L401 14 L401 40 Z" fill="var(--white)"/>
  </svg>

  <div class="abs brand-lockup back-logo"><span class="mark"></span><span class="name">LARKWOOD</span></div>
  <p class="abs call-title">Call Us Now For Your Free<br>Colour Consultation</p>
  <div class="abs call-pill">
    <svg width="16" height="17" viewBox="0 0 16 17" aria-hidden="true"><path d="M4 1 L6 5 L4.5 6.5 C5.5 9 7.5 11 10 12 L11.5 10.5 L15 12.5 L13.5 16 C7 15.5 1.5 10 1 3 Z" fill="var(--white)"/></svg>
    Call Us Now On 1300 555 018
  </div>
  <p class="abs contact" style="top:951px">
    <svg width="9" height="9" viewBox="0 0 10 10" aria-hidden="true"><circle cx="5" cy="5" r="4.3" fill="none" stroke="var(--brand)" stroke-width="1"/><path d="M.7 5h8.6M5 .7c2.4 2.4 2.4 6.2 0 8.6M5 .7c-2.4 2.4-2.4 6.2 0 8.6" fill="none" stroke="var(--brand)" stroke-width=".8"/></svg>
    https://larkwoodresurfacing.com.au/
  </p>
  <p class="abs contact" style="top:964px">
    <svg width="9" height="8" viewBox="0 0 10 8" aria-hidden="true"><rect x=".5" y=".5" width="9" height="7" fill="var(--brand)"/><path d="M.5 .5 L5 4.5 L9.5 .5" fill="none" stroke="var(--white)" stroke-width=".8"/></svg>
    admin@larkwoodresurfacing.com.au
  </p>
  <div class="abs urgency">Act Now -Offer Ending Soon!</div>
</section>

</body>
</html>
```